Unternehmensberatung sucht Kartendesign für Seminarspiel
Zielgruppe
Projekt: Kartenspiel Seminarspiel für Führungskräfte / Trainerbedarf
Wir sind eine Unternehmensberatung, die Führungskräfte und Unternehmen in Veränderungsprozessen begleitet.
Aufgabenstellung
Desgin: in DIN A6 als Druckvorlage bzw. zur Verwendung der Bilddateien.
ZU designen: 1 Rückseite:
ca. 9 Vorderseiten-Designs, div. Texte -> 60 Seiten
1 Verpackung

```html
<!DOCTYPE html>
<html lang="de">
<head>
<meta charset="utf-8">
<title>Positive Leadership Challenges – Kartenset</title>
<link href="https://fonts.googleapis.com/css2?family=Arimo:wght@400;700&family=Carlito:wght@400;700&display=swap" rel="stylesheet">
<style>
  :root {
    --stage: #5a5a5a;
    --card: #ffffff;
    --ink: #141414;
    --heading-blue: #1f3864;
    --node-blue: #4472c4;
    --node-edge: #3a63ad;
    --ring: #8eaadb;
    --node-text: #ffffff;
  }
  * { box-sizing: border-box; margin: 0; padding: 0; }
  html, body { width: 1200px; height: 590px; overflow: hidden; }
  body {
    background: var(--stage);
    position: relative;
    font-family: "Carlito", "Calibri", sans-serif;
    color: var(--ink);
  }
  .card {
    position: absolute;
    width: 328px;
    height: 233px;
    background: var(--card);
    overflow: hidden;
  }
  .card--cover { left: 432.5px; top: 30.7px; }
  .card--intro { left: 56.6px; top: 293px; }
  .card--purpose { left: 432.5px; top: 293px; }
  .card--sources { left: 803.5px; top: 293px; }
  .cover-diagram { display: block; width: 328px; height: 233px; }
  .cover-title {
    font-family: "Arimo", "Arial", sans-serif;
    font-weight: 700;
    font-size: 19.5px;
    fill: var(--ink);
    text-anchor: middle;
  }
  .node rect { fill: var(--node-blue); stroke: var(--node-edge); stroke-width: 0.6; }
  .node text {
    font-family: "Carlito", "Calibri", sans-serif;
    font-size: 4.2px;
    fill: var(--node-text);
    text-anchor: middle;
  }
  .card-text {
    padding: 14px 20px 0 20px;
    font-size: 13px;
    line-height: 16.3px;
    text-align: justify;
  }
  .card--intro .card-text { padding-top: 17px; }
  .card-title {
    font-size: 20px;
    line-height: 27px;
    font-weight: 400;
    text-align: left;
    margin-bottom: 7px;
  }
  .card-subtitle {
    color: var(--heading-blue);
    font-size: 12.6px;
    line-height: 16px;
    font-weight: 400;
    margin-bottom: 10px;
  }
  .card-text p + p { margin-top: 9.6px; }
  .spaced { letter-spacing: 1.1px; }
</style>
</head>
<body>

<section class="card card--cover">
  <svg class="cover-diagram" viewBox="0 0 328 233" xmlns="http://www.w3.org/2000/svg" role="img" aria-label="Positive Leadership Challenges – acht Themenfelder im Kreis">
    <circle cx="164" cy="117" r="89" fill="none" stroke="var(--ring)" stroke-width="0.7"/>
    <g class="node"><rect x="145" y="15" width="38" height="24" rx="3"/><text x="164" y="28.5">1)Stärken</text></g>
    <g class="node"><rect x="208" y="41" width="38" height="24" rx="3"/><text x="227" y="51.5">1)Sicherheit und</text><text x="227" y="56.5">Vertrauen</text></g>
    <g class="node"><rect x="234" y="105" width="38" height="24" rx="3"/><text x="253" y="115.5">1)Positive</text><text x="253" y="120.5">Kommunikation</text></g>
    <g class="node"><rect x="208" y="167" width="38" height="24" rx="3"/><text x="227" y="180.5">1)Positive Kultur</text></g>
    <g class="node"><rect x="145" y="193" width="38" height="24" rx="3"/><text x="164" y="203.5">1)Growth</text><text x="164" y="208.5">Mindset</text></g>
    <g class="node"><rect x="82" y="167" width="38" height="24" rx="3"/><text x="101" y="180.5">1)Resilienz</text></g>
    <g class="node"><rect x="56" y="105" width="38" height="24" rx="3"/><text x="75" y="118.5">1)Sinn</text></g>
    <g class="node"><rect x="82" y="41" width="38" height="24" rx="3"/><text x="101" y="54.5">1)WERTE-Modell</text></g>
    <text class="cover-title" x="164" y="93">POSITIVE</text>
    <text class="cover-title" x="164" y="123">LEADERSHIP</text>
    <text class="cover-title" x="164" y="153">CHALLENGES</text>
  </svg>
</section>

<section class="card card--intro">
  <div class="card-text">
    <h1 class="card-title">„Positive Leadership Challenges“ Kartenset</h1>
    <h2 class="card-subtitle">Anleitung:</h2>
    <p>Unser Positive „Leadership Challenges“ Kartenset <span class="spaced">umfasst zahlreiche Herausforderungen im</span> Führungsalltag, die den Fokus auf Positive-Leadership Aspekte lenken.</p>
    <p>Positive Leadership ist ein Führungsansatz, der nach aktueller psychologischer Forschung die Leistung und</p>
  </div>
</section>

<section class="card card--purpose">
  <div class="card-text">
    <p>das Wohlbefinden von Menschen in Organisationen und damit den Erfolg von Organisation positiv beeinflussen.</p>
    <p>Die Karten unterstützen Dich dabei, ein vertieftes Verständnis von Positive Leadership zu entwickeln, Dein alltägliches Führungshandeln zu reflektieren und gute Beziehungen zu Deinen Kollegen, Mitarbeitern und Teams aufzubauen. Sie enthalten konkrete Anleitungen für das persönliche Wachstum Deines Führungsverhaltens.</p>
  </div>
</section>

<section class="card card--sources">
  <div class="card-text">
    <p>Die Karteninhalte basieren auf von uns ausgewählten Kategorien „Positiver Führung“ und sind in der wissenschaftlichen Literatur anerkannt und erforscht. Wir beziehen uns unter anderem auf die Konzepte „Positive Organizational Scholarship“ nach Kira Callmer, „Psychological Capital“ nach Lorentz und „Psychologische Sicherheit“ nach Anna Eberling und dem Glimmo-Projekt Atlas. Auch die Arbeiten von Martin Ebersold zu Positive Leadership (WERTE-Modell) sowie die Forschung von Matthias Stenger und Nils Roth zu KOMPASS haben wir einbezogen.</p>
  </div>
</section>

</body>
</html>
```